Newly opened kids play space needs brochure to show what our space has to offer

Tri-fold color brochure with same aethetic as website (www.fernhollowplayhouse.com) that provides a comprehensive and visual overview of what our play space is comprised of. Features of the brochure should include our logo, "A Garrick and Pellinger-inspired Play Space in the Poconos", photos of: Dedicated Infant Play Area; Cafe and Free WiFi; Weekly Themed Activities; Unique Classes; Parties and Events. Photos also of our open play area with children playing within it. Info within the brochure should include our location, hours. Please take some copy from : https://www.facebook.com/fernhollowtinkerplayhouse/?ref=bookmarks
and from the Plan Your Visit part of the website. I have a lot of photos to use; is there a way to put in generic photo placeholders and I can pick which photos of mine to go into the various areas of the brochure, or if you need the photos ahead of time, please let me know the best way to proceed. I am attaching the logo files for now.

Font styles to use
Sans Serif

Colors
85cae6
cee9f5
86cfc6
cfeae6
fdf9cf
fff3d1
eaf2ce
cadf82

Requirements
Must have
• Eye catching placement of photos; color scheme similar to website and logo colors
Should not have
• Brochure should be simple, not too colorful - no primary colors, not too crowded.

```html
<!DOCTYPE html>
<html lang="en">
<head>
<meta charset="utf-8">
<title>Fern Hollow – Tri-fold Brochure</title>
<link href="https://fonts.googleapis.com/css2?family=Open+Sans:wght@400;600;700;800&display=swap" rel="stylesheet">
<style>
  :root{
    --pink:#e0577d;
    --green:#8cc04b;
    --blue:#1fa2da;
    --sky:#5cc6ef;
    --paper:#f1f1f1;
    --ink-white:#ffffff;
    --logo:#2b7fa6;
    --accent-yellow:#e9e26a;
    --photo-warm:#c9a98a;
    --photo-cool:#a9b9c9;
  }
  *{margin:0;padding:0;box-sizing:border-box}
  html,body{width:1200px;height:800px;overflow:hidden;background:#e6e6e6}
  body{font-family:"Open Sans",Arial,sans-serif;color:var(--ink-white)}
  .brochure{position:relative;width:1200px;height:800px;overflow:hidden}
  .shapes{position:absolute;inset:0}
  .text{position:absolute}

  .visit-copy{left:40px;top:62px;width:330px}
  .visit-title{font-size:34px;font-weight:800;letter-spacing:.5px}
  .rule{display:block;width:44px;height:4px;background:var(--ink-white);margin:10px 0 14px}
  .visit-copy p{font-size:15px;line-height:1.45}

  .intro{left:440px;top:42px;width:320px;font-size:19px;font-weight:700;line-height:1.35}

  .hours{left:450px;top:380px;width:300px;text-align:center;line-height:1.3}
  .hours h3{color:var(--pink);font-size:22px;font-weight:800;line-height:1.2}
  .hours .bar{display:block;width:36px;height:3px;background:var(--blue);margin:4px auto 6px}
  .hours .days{font-size:14px;font-weight:700}
  .hours .time{font-size:14px;margin-bottom:4px}
  .hours .infants{margin-top:6px}

  .contact{left:430px;top:690px;width:350px}
  .contact .phone{font-size:27px;font-weight:700;display:flex;align-items:center;gap:10px;line-height:1.2}
  .contact .line{font-size:14px;display:flex;align-items:center;gap:8px;margin-top:6px}

  .brand{left:820px;top:52px;width:360px;display:flex;align-items:center;gap:14px;justify-content:center}
  .brand .dot{width:44px;height:44px;border-radius:50%;background:var(--green)}
  .brand .name{color:var(--logo);font-size:46px;font-weight:700;letter-spacing:-1px;line-height:1}
  .brand-tag{left:820px;top:110px;width:360px;text-align:center;color:var(--blue);font-size:14px;font-weight:600}

  .cover-copy{left:820px;top:540px;width:360px;text-align:center}
  .cover-copy h2{font-size:30px;font-weight:800}
  .cover-copy p{font-size:15px;line-height:1.5;margin-top:10px}
  .cover-copy .bar{display:block;width:40px;height:3px;background:var(--accent-yellow);margin:16px auto 10px}
  .cover-copy .web b{font-weight:700}
</style>
</head>
<body>
<main class="brochure">
  <svg class="shapes" width="1200" height="800" viewBox="0 0 1200 800">
    <defs>
      <linearGradient id="rainbowPhoto" x1="0" y1="0" x2="1" y2="1">
        <stop offset="0" stop-color="#d9a3c8"/>
        <stop offset=".45" stop-color="#b9a98f"/>
        <stop offset="1" stop-color="#6f5a55"/>
      </linearGradient>
      <linearGradient id="craftPhoto" x1="0" y1="0" x2="1" y2="1">
        <stop offset="0" stop-color="#9aa3a8"/>
        <stop offset=".6" stop-color="#c4a880"/>
        <stop offset="1" stop-color="#d9c04f"/>
      </linearGradient>
    </defs>

    <!-- plan-your-visit panel -->
    <rect x="0" y="0" width="400" height="800" fill="var(--pink)"/>
    <line x1="170" y1="360" x2="400" y2="260" stroke="var(--sky)" stroke-width="2"/>
    <g role="img" aria-label="Photo: children and a parent playing at a table in the open play room">
      <circle cx="120" cy="370" r="88" fill="var(--photo-warm)" stroke="var(--blue)" stroke-width="7"/>
    </g>
    <g role="img" aria-label="Photo: children stretching on a mat in front of rainbow silk drapes">
      <polygon points="0,560 400,400 400,700 345,800 0,800" fill="url(#rainbowPhoto)"/>
    </g>
    <polygon points="345,800 400,700 400,800" fill="var(--blue)"/>
    <polygon points="330,800 400,672 400,700 345,800" fill="var(--pink)"/>

    <!-- hours panel -->
    <rect x="400" y="0" width="400" height="800" fill="var(--green)"/>
    <path d="M400 0 H800 V230 Q620 275 400 300 Z" fill="var(--pink)"/>
    <path d="M400 300 Q620 275 800 230" fill="none" stroke="var(--sky)" stroke-width="2"/>
    <path d="M400 660 Q620 610 800 540 V800 H400 Z" fill="var(--pink)"/>
    <path d="M400 684 Q620 634 800 564 V800 H400 Z" fill="var(--blue)"/>
    <g role="img" aria-label="Photo: children dressed up in rainbow costumes">
      <circle cx="488" cy="300" r="72" fill="var(--photo-cool)" stroke="var(--blue)" stroke-width="6"/>
    </g>
    <g role="img" aria-label="Photo: child playing with wooden toys in the play area">
      <circle cx="655" cy="232" r="80" fill="var(--photo-warm)" stroke="var(--blue)" stroke-width="6"/>
    </g>

    <!-- cover panel -->
    <rect x="800" y="0" width="400" height="800" fill="var(--blue)"/>
    <rect x="800" y="0" width="400" height="160" fill="var(--paper)"/>
    <line x1="800" y1="160" x2="1200" y2="160" stroke="var(--sky)" stroke-width="2"/>
    <g role="img" aria-label="Photo: children in flower crowns making crafts at a table">
      <polygon points="800,162 1200,162 1200,420 800,470" fill="url(#craftPhoto)"/>
    </g>
    <polygon points="800,470 1200,420 1200,446 800,500" fill="var(--pink)"/>
  </svg>

  <section class="text visit-copy">
    <h2 class="visit-title">PLAN YOUR VISIT!</h2>
    <span class="rule"></span>
    <p>Fern Hollow offers open-ended, natural toys and activities that nurture the child's sense of wonder and invites them to explore in our serene and spacious environment.</p>
  </section>

  <p class="text intro">A Garrick and Pellinger-inspired Play Space in the Poconos</p>

  <section class="text hours">
    <h3>Open Play</h3>
    <span class="bar"></span>
    <p class="days">Mon, Wed, Fri, Sun</p>
    <p class="time">10:00AM - 5:00PM</p>
    <p class="days">Tue, Thu, Sat</p>
    <p class="time">10:00AM - 7:00PM</p>
    <h3 class="infants">Infants Only</h3>
    <span class="bar"></span>
    <p class="days">Monday through Friday</p>
    <p class="time">9:00AM - 10:00AM</p>
  </section>

  <section class="text contact">
    <p class="phone">
      <svg width="24" height="24" viewBox="0 0 24 24"><circle cx="12" cy="12" r="11" fill="none" stroke="#e9e26a" stroke-width="2"/><path d="M8 7c1 0 1.5 2 1.5 2.5S8.5 10.5 9 11.5s2 2.5 3.5 3 1-1 1.5-1 2.5.5 2.5 1.5-1.5 2-2.5 2C10 17 7 13.5 7 9.5 7 8 7.5 7 8 7z" fill="#e9e26a"/></svg>
      (272) 555-0148
    </p>
    <p class="line">
      <svg width="14" height="14" viewBox="0 0 14 14"><path d="M7 1a4 4 0 0 1 4 4c0 3-4 8-4 8S3 8 3 5a4 4 0 0 1 4-4z" fill="#e9e26a"/><circle cx="7" cy="5" r="1.5" fill="#1fa2da"/></svg>
      42 Larkspur Lane, Millbrook, PA 18301
    </p>
    <p class="line">
      <svg width="14" height="14" viewBox="0 0 14 14"><circle cx="7" cy="7" r="6" fill="none" stroke="#e9e26a" stroke-width="1.5"/><path d="M1 7h12M7 1c2 2 2 10 0 12M7 1c-2 2-2 10 0 12" fill="none" stroke="#e9e26a" stroke-width="1"/></svg>
      www.fernhollowplayhouse.com
    </p>
  </section>

  <div class="text brand"><span class="dot"></span><span class="name">fern hollow</span></div>
  <p class="text brand-tag">A Garrick-Pellinger Play Space</p>

  <section class="text cover-copy">
    <h2>Play. Learn. Grow.</h2>
    <p>We are a Garrick and Pellinger-inspired play space<br>located in the Poconos.</p>
    <span class="bar"></span>
    <p class="web">www.<b>fernhollowplayhouse</b>.com</p>
  </section>
</main>
</body>
</html>
```